Poster design for - Glowing Meadow Festival

To design a dynamic illustrated Glowing Meadow Festival poster.
The dates are: 3-5 July 2020
Location: Tarlow Campsite, Ashcombe, Marlshire
www.glowingmeadow.co.uk

Here is some text about the event to give you an idea. You can take elements from it if you like:

A Gathering of Female Energy to Ignite and Embrace the Power of Woman with Mother Earth.

Target Market(s)

Women festival goers.

Industry/Entity Type

Festival

Colors

Designer to choose colors to be used in the design.

Requirements
Must have
• Glowing Meadow Logo - but this can be altered to look washed out.
• Date, location, website url.
Nice to have
• Earthy, hippy, festival look.

```html
<!DOCTYPE html>
<html lang="en">
<head>
<meta charset="utf-8">
<title>Glowing Meadow Festival Poster</title>
<link rel="stylesheet" href="https://fonts.googleapis.com/css2?family=Marcellus&family=Oswald:wght@500;600&display=swap">
<style>
  :root {
    --cream: #eef0e2;
    --ink: #1c1a1e;
    --flame: #e2501f;
    --flame-deep: #d9431a;
    --glow: #f6d35a;
    --plum: #5a2a5c;
    --magenta: #b0365e;
    --teal: #4f8c92;
    --white: #ffffff;
  }
  * { margin: 0; padding: 0; box-sizing: border-box; }
  html, body { width: 800px; height: 1200px; overflow: hidden; background: var(--cream); }
  .poster {
    position: relative;
    width: 800px;
    height: 1200px;
    overflow: hidden;
    background: linear-gradient(180deg, #f1f2e6 0%, var(--cream) 45%, #e8e6d6 100%);
  }
  .artwork {
    position: absolute;
    left: 0; top: 470px;
    width: 800px; height: 730px;
    background:
      radial-gradient(circle at 640px 170px, rgba(255,246,190,0.95) 0, rgba(246,211,90,0.85) 60px, rgba(232,110,40,0.75) 140px, rgba(176,54,94,0.35) 200px, rgba(176,54,94,0) 240px),
      radial-gradient(ellipse at 620px 560px, rgba(79,140,146,0.55) 0, rgba(79,140,146,0) 260px),
      radial-gradient(ellipse at 170px 420px, rgba(90,42,92,0.85) 0, rgba(90,42,92,0.4) 220px, rgba(90,42,92,0) 320px),
      linear-gradient(180deg, rgba(238,240,226,0) 0%, rgba(176,54,94,0.35) 55%, rgba(90,42,92,0.9) 100%);
  }
  .brand {
    position: absolute;
    top: 110px; left: 0; width: 800px;
    display: flex; align-items: center; justify-content: center; gap: 16px;
  }
  .brand-dot {
    width: 30px; height: 30px; border-radius: 50%;
    background: var(--flame);
  }
  .brand-name {
    font-family: "Marcellus", serif;
    font-size: 52px;
    letter-spacing: 3px;
    color: var(--flame);
    text-transform: uppercase;
  }
  .headline {
    position: absolute;
    top: 300px; left: 0; width: 800px;
    text-align: center;
    font-family: "Marcellus", serif;
    font-weight: 400;
    color: var(--ink);
    line-height: 1.2;
  }
  .headline .line { display: block; }
  .headline .sm { font-size: 30px; }
  .headline .md { font-size: 42px; }
  .headline .lg { font-size: 50px; }
  .details {
    position: absolute;
    left: 110px; top: 900px;
    width: 580px; height: 150px;
    transform: rotate(-4deg);
    background: var(--flame-deep);
    border-radius: 6px 40px 8px 30px;
    display: flex; flex-direction: column; align-items: center; justify-content: center;
    font-family: "Oswald", sans-serif;
    color: var(--white);
    text-align: center;
    line-height: 1.25;
  }
  .details .date { font-size: 30px; font-weight: 600; letter-spacing: 1px; }
  .details .venue { font-size: 32px; font-weight: 600; }
  .details .url { font-size: 24px; font-weight: 500; }
</style>
</head>
<body>
  <main class="poster">
    <div class="artwork" role="img" aria-label="Illustration of a woman holding up a glowing Earth, with fiery light trails over a soft sky"></div>

    <header class="brand">
      <span class="brand-dot"></span>
      <span class="brand-name">Glowing Meadow</span>
    </header>

    <h1 class="headline">
      <span class="line sm">A Gathering of</span>
      <span class="line md">Female Energy to Ignite</span>
      <span class="line sm">and Embrace</span>
      <span class="line md">the Power of Woman</span>
      <span class="line md"><span class="sm">with</span> <span class="lg">Mother Earth</span></span>
    </h1>

    <section class="details">
      <p class="date">3 – 5 JULY 2020</p>
      <p class="venue">Tarlow Campsite | Ashcombe | Marlshire</p>
      <p class="url">www.glowingmeadow.co.uk</p>
    </section>
  </main>
</body>
</html>
```